I am looking for a modern style design for a podcast cover art.
Titled: Open Harbor with R.K. Thistlewood
colors to stay in the grays, reds, blacks, white, gold, and maybe blues if it fits well. I attached a mock up of what we are going for and a current podcast cover we drew inspiration from.
Colors
3276b5
ec1f27
f04a50
1b1b1b
474747
919191
d2d2d2

```html
<!DOCTYPE html>
<html lang="en">
<head>
<meta charset="UTF-8">
<title>Open Harbor with R.K. Thistlewood — Podcast Cover</title>
<link href="https://fonts.googleapis.com/css2?family=Archivo+Black&family=Montserrat:wght@300;800&display=swap" rel="stylesheet">
<style>
  :root {
    --blue: #3276b5;
    --red: #ec1f27;
    --ink: #1b1b1b;
    --charcoal: #474747;
    --gray: #919191;
    --silver: #d2d2d2;
    --paper: #ececec;
  }
  * { margin: 0; padding: 0; box-sizing: border-box; }
  html, body { width: 1200px; height: 671px; overflow: hidden; background: var(--paper); }
  .cover {
    position: relative;
    width: 1200px;
    height: 671px;
    overflow: hidden;
    background: var(--paper);
  }
  .backdrop { position: absolute; inset: 0; width: 1200px; height: 671px; }
  .title-block { font-weight: normal; }
  .title {
    position: absolute;
    left: 122px;
    color: var(--ink);
    line-height: 1;
    white-space: nowrap;
  }
  .title-light {
    top: 176px;
    font-family: "Montserrat", sans-serif;
    font-weight: 300;
    font-size: 146px;
    letter-spacing: 1px;
  }
  .title-heavy {
    top: 312px;
    font-family: "Archivo Black", sans-serif;
    font-size: 168px;
    letter-spacing: -3px;
  }
  .host {
    position: absolute;
    right: 295px;
    top: 542px;
    text-align: right;
    color: var(--ink);
    font-family: "Montserrat", sans-serif;
    font-weight: 800;
  }
  .host-with {
    display: block;
    font-size: 15px;
    font-style: italic;
    letter-spacing: 0.5px;
  }
  .host-name {
    display: block;
    font-size: 31px;
    letter-spacing: -0.5px;
    margin-top: 2px;
  }
</style>
</head>
<body>
<main class="cover">
  <svg class="backdrop" viewBox="0 0 1200 671">
    <defs>
      <linearGradient id="paperSheen" x1="0" y1="0" x2="1" y2="0">
        <stop offset="0" stop-color="#e9e9e9"/>
        <stop offset="1" stop-color="#f3f3f3"/>
      </linearGradient>
      <linearGradient id="ridgeFade" x1="0" y1="0" x2="0" y2="1">
        <stop offset="0" stop-color="#c81a20"/>
        <stop offset="0.55" stop-color="#b5161c"/>
        <stop offset="1" stop-color="#6e0c10"/>
      </linearGradient>
      <linearGradient id="photoTone" x1="0" y1="0" x2="1" y2="1">
        <stop offset="0" stop-color="#8a8a8a"/>
        <stop offset="0.5" stop-color="#474747"/>
        <stop offset="1" stop-color="#1b1b1b"/>
      </linearGradient>
    </defs>

    <rect class="paper" width="1200" height="671" fill="url(#paperSheen)"/>
    <polygon class="paper-band" points="915,0 1200,0 1200,671 745,671" fill="#f1f1f1"/>

    <polygon class="red-field" points="0,0 225,0 700,671 0,671"
             fill="url(#ridgeFade)" role="img"
             aria-label="Red-toned photograph of layered mountain ridges fading into haze"/>

    <polygon class="blue-wedge" points="223,0 580,0 404,240" fill="var(--blue)"/>

    <rect class="host-photo" x="940" y="50" width="260" height="621"
          fill="url(#photoTone)" role="img"
          aria-label="Black-and-white photograph of the host in formal evening wear, gesturing toward the title"/>
  </svg>

  <h1 class="title-block">
    <span class="title title-light">OPEN</span>
    <span class="title title-heavy">HARBOR</span>
  </h1>

  <p class="host">
    <span class="host-with">WITH</span>
    <span class="host-name">R.K. Thistlewood</span>
  </p>
</main>
</body>
</html>
```